Marrowind Booking Engine Marketing Site

Hi,
I’m currently in the process of putting together a web application with the intention of providing small resorts/B&Bs/small hotels the ability to allow their customers to book online.
I’m looking to have a design created for a marketing site, to give potential customers additional information about my booking engine, as well as to help drive sign-ups. A lot of the competition out there appears outdated, so I would like something that is more modern and up to date.
I am looking for just the design (i’m a web developer, but I lack the creative skills for a good marketing site)
For some more background, I will be targeting business owners of smaller resorts and Bed & Breakfasts. These are typically family owned small businesses that may only have a 10 room setup. These businesses will also typically have additional amenities that they will have to rent out or sell to their clients ( ex. Spa, fruit basket, water sport rentals). My software will provide them with the ability to sell their amenities as well.
I’m open to different designs, but my main thing is I want it to look modern, and I want it to have several callouts to sign up for my product.
I am looking to have the homepage created, 1 interior page, and a style guide created (to show form fields, H1’s, etc.).
I had a logo created a couple months ago that will be included with this project brief.
If you need any additional information feel free to reach out to me.

Target Market(s)

This site will be targeted small business owners who are running small resorts, Bed and Breakfasts, or any business that provides rooms for their clients.

Industry/Entity Type

Saas

Number of Pages Required

2 page

Font styles to use
Sans Serif

Colors

Designer to choose colors to be used in the design.

Requirements
Must have
• A modern feel, with several CTA's that will drive to the registration page on the homepage. on the internal page, I mostly just need the page layout, I will reuse that page layout. and a style guide if at all possible (include colors, form fields, H1's, etc.)
Nice to have
• maybe a hero image at the top with buttons over the top? again i'm pretty open to most anything.
Should not have
• I like images, but I don't want the page overrun with images. A good balance.

```html
<!DOCTYPE html>
<html lang="en">
<head>
<meta charset="utf-8">
<title>Marrowind Booking Engine</title>
<link href="https://fonts.googleapis.com/css2?family=Montserrat:wght@400;500;600;700&display=swap" rel="stylesheet">
<style>
:root{
  --blue:#0d4a86;
  --blue-dark:#0a3b6e;
  --green:#7ab800;
  --green-dark:#5f9200;
  --text:#333;
  --grey:#6d6d6d;
  --white:#fff;
}
*{margin:0;padding:0;box-sizing:border-box}
html,body{width:732px;height:1200px;overflow:hidden;background:#fff}
body{font-family:'Montserrat',sans-serif;color:var(--text);position:relative}
.abs{position:absolute}
.pill{position:absolute;border-radius:12px;background:var(--blue);color:var(--white);font-size:10px;display:flex;align-items:center;justify-content:center}

/* header */
.brand{left:61px;top:13px;display:flex;align-items:center;gap:6px}
.brand-mark{width:32px;height:32px;border-radius:50%;background:var(--green)}
.brand-name{font-size:20px;color:var(--blue);line-height:20px;font-weight:500}
.brand-sub{font-size:13px;color:var(--grey);line-height:14px;letter-spacing:.3px}
.signup{left:570px;top:21px;width:67px;height:19px}
.menu{left:648px;top:25px;width:14px}
.menu span{display:block;height:1.3px;background:var(--blue);margin-bottom:4px}

/* nav */
.nav{left:0;top:60px;width:732px;height:32px;background:var(--green)}
.nav a{position:absolute;top:11px;color:var(--white);font-size:10px;text-decoration:none}
.search{left:640px;top:64px;width:24px;height:24px;border-radius:50%;background:var(--green-dark)}

/* hero */
.hero{left:61px;top:101px;width:610px;height:263px;background:linear-gradient(100deg,#3a2418 0%,#6b3a2a 35%,#8a5a44 55%,#2f3e4a 75%,#5a8ea0 100%)}
.hero h1{position:absolute;left:35px;top:68px;font-size:19px;font-weight:400;color:var(--white)}
.hero p{position:absolute;left:35px;top:97px;width:300px;font-size:8.6px;line-height:15.6px;color:var(--white)}
.hero .pill{left:35px;top:150px;width:85px;height:21px}
.dots{position:absolute;left:40px;top:207px;display:flex;gap:8px}
.dots i{width:8px;height:8px;border-radius:50%;background:var(--green)}
.dots i.on{background:#fff;border:2px solid var(--green)}

/* sections */
.welcome{left:0;top:384px;width:732px;text-align:center}
.welcome h2{font-size:14.5px;font-weight:400;color:var(--blue)}
.welcome h2 b{font-weight:700}
.welcome p{font-size:8.4px;line-height:16px;margin-top:9px;color:var(--text)}

.feat-img{left:61px;top:485px;width:269px;height:203px;background:linear-gradient(120deg,#071a3a 0%,#0c3b7a 45%,#1a8ac0 75%,#0a2450 100%)}
.features{left:369px;top:490px;width:276px}
.features h2{font-size:14.5px;font-weight:400;color:var(--blue)}
.features p{font-size:8.4px;line-height:16px;margin-top:8px;text-align:justify}
.features ul{list-style:none;margin-top:14px}
.features li{font-size:7.8px;color:var(--blue);height:19px;padding-left:19px;position:relative}
.features li svg{position:absolute;left:0;top:1px}
.features .pill{left:-3px;top:159px;width:85px;height:21px}

.owners{left:0;top:724px;width:732px;text-align:center;font-size:14.5px;color:var(--blue)}
.card-img{top:770px;width:293px;height:151px}
.card-title{top:932px;font-size:15.5px;color:var(--blue);letter-spacing:.3px}
.card-text{top:956px;width:293px;font-size:7.8px;line-height:13px;text-align:justify}

/* footer */
.footer{left:0;top:1016px;width:732px;height:146px;background:linear-gradient(100deg,#0e4a88 0%,#135696 60%,#2a6aa2 100%)}
.f-head{font-size:9px;font-weight:600;color:var(--white);letter-spacing:1.2px;text-decoration:underline;text-underline-offset:3px}
.f-small{font-size:5.8px;line-height:9.3px;color:var(--white)}
.social{display:flex;gap:6px}
.social i{width:16px;height:16px;border-radius:50%;border:1px solid var(--white)}
.email{left:518px;top:1092px;width:154px;height:18px;border:1px solid #b9c9dc;border-radius:9px;font-size:7.8px;color:var(--white);padding:4px 0 0 10px}
.subscribe{left:518px;top:1119px;width:71px;height:18px;border-radius:9px;background:var(--green);color:var(--white);font-size:7px;font-weight:700;display:flex;align-items:center;justify-content:center}
.bottom{left:0;top:1162px;width:732px;height:38px;background:var(--blue-dark);color:var(--white);font-size:7.4px}
.bottom .links{position:absolute;left:64px;top:15px;word-spacing:2px}
.bottom .copy{position:absolute;left:542px;top:14px}
</style>
</head>
<body>

<header>
  <div class="abs brand">
    <div class="brand-mark"></div>
    <div>
      <div class="brand-name">MARROWIND</div>
      <div class="brand-sub">BOOKING ENGINE</div>
    </div>
  </div>
  <div class="pill signup">Sign-up</div>
  <div class="abs menu"><span></span><span></span><span></span></div>
</header>

<nav class="abs nav">
  <a style="left:78px">Home</a>
  <a style="left:128px">About Us</a>
  <a style="left:193px">Features</a>
  <a style="left:255px">Bookings</a>
  <a style="left:321px">Blog</a>
  <a style="left:364px">Contact Us</a>
</nav>
<div class="abs search">
  <svg width="24" height="24" viewBox="0 0 24 24"><circle cx="11" cy="11" r="3.5" fill="none" stroke="#fff" stroke-width="1.6"/><line x1="13.6" y1="13.6" x2="16" y2="16" stroke="#fff" stroke-width="1.8"/></svg>
</div>

<section class="abs hero" role="img" aria-label="Hand typing on a laptop showing a hotel deals booking page">
  <h1>Marrowind Booking Engine</h1>
  <p>We are in the process of putting together a web application with the intention of providing small resorts/B&amp;Bs/small hotels the ability to allow their customers to book online</p>
  <div class="pill">Get Started</div>
  <div class="dots"><i></i><i class="on"></i><i></i><i></i></div>
</section>

<section class="abs welcome">
  <h2>Welcome To <b>Marrowind Booking Engine</b></h2>
  <p>Sed ut perspiciatis unde omnis iste natus error sit voluptatem accusantium doloremque laudantium, totam rem aperiam,<br>eaque ipsa quae ab illo inventore veritatis et quasi architecto beatae vitae dicta sunt explicabo.</p>
</section>

<div class="abs feat-img" role="img" aria-label="Lines of program code glowing on a blue screen"></div>
<section class="abs features">
  <h2>Our Features</h2>
  <p>Sed ut perspiciatis unde omnis iste natus error sit voluptatem accusantium doloremque laudantium, totam rem aperiam...</p>
  <ul>
    <li><svg width="10" height="6" viewBox="0 0 10 6"><path d="M0 3h8M6 1l2 2-2 2" fill="none" stroke="#0d4a86" stroke-width="1.2"/></svg>Quis autem vel eum iure</li>
    <li><svg width="10" height="6" viewBox="0 0 10 6"><path d="M0 3h8M6 1l2 2-2 2" fill="none" stroke="#0d4a86" stroke-width="1.2"/></svg>Nor again is there anyone</li>
    <li><svg width="10" height="6" viewBox="0 0 10 6"><path d="M0 3h8M6 1l2 2-2 2" fill="none" stroke="#0d4a86" stroke-width="1.2"/></svg>Nam libero tempore,</li>
    <li><svg width="10" height="6" viewBox="0 0 10 6"><path d="M0 3h8M6 1l2 2-2 2" fill="none" stroke="#0d4a86" stroke-width="1.2"/></svg>Omnis dolor repellendus.</li>
  </ul>
  <div class="pill">Get Started</div>
</section>

<h2 class="abs owners" style="font-weight:400">Our Business Owners</h2>

<div class="abs card-img" style="left:61px;background:linear-gradient(160deg,#e8a040 0%,#8a6a50 40%,#4a4a48 75%,#2a3038 100%)" role="img" aria-label="Harbour village with cottages at sunset"></div>
<div class="pill" style="left:159px;top:835px;width:85px;height:21px">Read more</div>
<div class="abs card-title" style="left:63px">SMALLER RESORTS</div>
<p class="abs card-text" style="left:63px">Neque porro quisquam est, qui dolorem ipsum quia dolor sit amet, consectetur, adipisci velit, sed quia non numquam eius modi tempora</p>

<div class="abs card-img" style="left:379px;background:linear-gradient(100deg,#d8c8b0 0%,#6a3a28 45%,#2a1a14 70%,#8a7060 100%)" role="img" aria-label="Folded napkin and wine glasses on a set table"></div>
<div class="pill" style="left:474px;top:835px;width:85px;height:21px">Read more</div>
<div class="abs card-title" style="left:377px">BED &amp; BREAKFASTS</div>
<p class="abs card-text" style="left:377px">Neque porro quisquam est, qui dolorem ipsum quia dolor sit amet, consectetur, adipisci velit, sed quia non numquam eius modi tempora</p>

<footer class="abs footer" role="img" aria-label="Faint tropical beach scene behind the footer">
  <div class="abs f-head" style="left:62px;top:28px">CONTACT US</div>
  <svg class="abs" style="left:60px;top:54px" width="6" height="8" viewBox="0 0 6 8"><path d="M3 8C1 5 0 4 0 3a3 3 0 0 1 6 0c0 1-1 2-3 5z" fill="#fff"/><circle cx="3" cy="3" r="1" fill="#135696"/></svg>
  <div class="abs f-small" style="left:74px;top:54px">Marrowind Booking Engine<br>#123 Lorium ipsum<br>Westbrook.<br>WB-20417.</div>
  <svg class="abs" style="left:60px;top:101px" width="8" height="8" viewBox="0 0 8 8"><path d="M1 0l2 2-1 1.2c.8 1.4 1.6 2.2 2.8 2.8L6 5l2 2-1 1C3.5 7.5.5 4.5 0 1z" fill="#fff"/></svg>
  <div class="abs f-small" style="left:74px;top:101px">Phone: 1-800 555 0142</div>
  <svg class="abs" style="left:60px;top:117px" width="9" height="8" viewBox="0 0 9 8"><rect x="0.5" y="2" width="8" height="5.5" fill="none" stroke="#fff"/><rect x="2" y="0.5" width="5" height="2" fill="none" stroke="#fff"/></svg>
  <div class="abs f-small" style="left:74px;top:117px">Fax: 555 01 42019</div>

  <div class="abs f-head" style="left:305px;top:30px">CONNECT WITH US</div>
  <div class="abs social" style="left:305px;top:54px"><i></i><i></i><i></i><i></i><i></i></div>

  <div class="abs f-head" style="left:519px;top:30px">NEWSLETTER</div>
  <div class="abs f-small" style="left:518px;top:48px;font-weight:600;width:150px;line-height:8px;font-size:6.4px">Stay up-to-date with quarterly news and updates</div>
  <svg class="abs" style="left:680px;top:118px" width="16" height="10" viewBox="0 0 16 10"><path d="M1 9l7-7 7 7" fill="none" stroke="#8fb0d0" stroke-width="1.6"/></svg>
</footer>
<div class="abs email">Enter your Email
  <svg class="abs" style="right:9px;top:5px" width="9" height="7" viewBox="0 0 9 7"><rect x="0.5" y="0.5" width="8" height="6" fill="none" stroke="#fff"/><path d="M0.5 0.5l4 3.5 4-3.5" fill="none" stroke="#fff"/></svg>
</div>
<div class="abs subscribe">SUBSCRIBE</div>

<div class="abs bottom">
  <div class="links">Home &nbsp;&nbsp;|&nbsp;&nbsp; About Us &nbsp;&nbsp;|&nbsp;&nbsp; Features &nbsp;&nbsp;|&nbsp;&nbsp; Blog &nbsp;&nbsp;|&nbsp;&nbsp; Contact Us</div>
  <div class="copy">© 2018 &nbsp;|&nbsp; Marrowind Booking Engine</div>
</div>

</body>
</html>
```